Business Card for my building company

I would like the card to make a statement, so as soon as you see the card you think "wow nice card' and then read the details on the card its self. Also i would like to be able to put in the detail for the MUST HAVES so please Crete a box that i can alter depending on who in my business needs the cards. Thank you

Target Market(s)

Any one looking to build a house/ townhouse or duplex

Industry/Entity Type

Home Builder

Contact Information for Business Card

I would like the card to have the logo on the card and the must haves

Font styles to use
Sans Serif

Requirements
Must have
• Name
• Phone Number
• Email Address
• Website
• Licence Number
• Abn

```html
<!DOCTYPE html>
<html lang="en">
<head>
<meta charset="utf-8">
<title>Ridgeline Builders – Business Card</title>
<link rel="stylesheet" href="https://fonts.googleapis.com/css2?family=Oswald:wght@500;700&family=Open+Sans:wght@400;600&display=swap">
<style>
  :root {
    --page-bg: #e7e4df;
    --stone-light: #8e8e8e;
    --stone-mid: #626262;
    --stone-dark: #3a3a3a;
    --gold: #d9b13b;
    --white: #f4f4f4;
    --muted: #dcdcdc;
  }
  * { box-sizing: border-box; margin: 0; padding: 0; }
  html, body {
    width: 1200px; height: 1023px; overflow: hidden;
    background: var(--page-bg);
  }
  .stage {
    width: 1200px; height: 1023px;
    display: flex; align-items: center; justify-content: center;
  }
  .card {
    position: relative;
    width: 900px; height: 540px;
    border-radius: 26px;
    overflow: hidden;
    box-shadow: 0 10px 30px rgba(0,0,0,.25);
  }
  .card__texture {
    position: absolute; inset: 0;
    background:
      radial-gradient(ellipse at 70% 30%, var(--stone-light) 0%, transparent 60%),
      linear-gradient(135deg, var(--stone-mid) 0%, var(--stone-light) 45%, var(--stone-mid) 75%, var(--stone-dark) 100%);
  }
  .brand {
    position: absolute; left: 70px; top: 200px;
    display: flex; align-items: center; gap: 18px;
  }
  .brand__mark {
    width: 60px; height: 60px;
    background: var(--gold);
  }
  .brand__name {
    font-family: "Oswald", sans-serif;
    font-weight: 700;
    font-size: 44px;
    line-height: 1.05;
    color: var(--white);
    text-transform: uppercase;
    letter-spacing: 1px;
  }
  .divider {
    position: absolute; left: 470px; top: 120px;
    width: 3px; height: 300px;
    background: var(--gold);
  }
  .details {
    position: absolute; left: 510px; top: 118px;
    font-family: "Open Sans", sans-serif;
    color: var(--white);
  }
  .details__name {
    font-family: "Oswald", sans-serif;
    font-weight: 500;
    font-size: 36px;
    color: var(--gold);
    text-transform: uppercase;
    letter-spacing: 1px;
    line-height: 1.1;
  }
  .details__role {
    font-size: 17px; font-weight: 600;
    text-transform: uppercase;
    letter-spacing: 1px;
    margin: 4px 0 26px;
  }
  .contact-list { list-style: none; }
  .contact-list li {
    display: flex; align-items: center; gap: 12px;
    font-size: 18px; line-height: 1;
    margin-bottom: 16px;
  }
  .contact-list .icon {
    width: 24px; height: 24px; flex: none;
    background: var(--gold);
    border-radius: 3px;
    display: flex; align-items: center; justify-content: center;
  }
  .registrations {
    margin-top: 20px;
    font-size: 18px; font-weight: 600;
    line-height: 1.6;
  }
</style>
</head>
<body>
<main class="stage">
  <section class="card">
    <div class="card__texture" role="img" aria-label="Weathered grey brick wall texture"></div>

    <div class="brand">
      <span class="brand__mark"></span>
      <span class="brand__name">Ridgeline<br>Builders</span>
    </div>

    <div class="divider"></div>

    <div class="details">
      <p class="details__name">Dan Whitfield</p>
      <p class="details__role">Director</p>
      <ul class="contact-list">
        <li>
          <span class="icon">
            <svg width="14" height="14" viewBox="0 0 24 24" aria-hidden="true"><path fill="#3a3a3a" d="M6.6 10.8a15 15 0 006.6 6.6l2.2-2.2a1 1 0 011-.25 11.4 11.4 0 003.6.6 1 1 0 011 1V20a1 1 0 01-1 1A17 17 0 013 4a1 1 0 011-1h3.5a1 1 0 011 1 11.4 11.4 0 00.6 3.6 1 1 0 01-.25 1z"/></svg>
          </span>555-210-4837
        </li>
        <li>
          <span class="icon">
            <svg width="14" height="14" viewBox="0 0 24 24" aria-hidden="true"><path fill="#3a3a3a" d="M2 5h20v14H2z"/><path fill="none" stroke="#d9b13b" stroke-width="2" d="M2 6l10 7 10-7"/></svg>
          </span>danwhitfield@ridgelinebuild.com
        </li>
        <li>
          <span class="icon">
            <svg width="14" height="14" viewBox="0 0 24 24" aria-hidden="true"><circle cx="12" cy="12" r="9" fill="none" stroke="#3a3a3a" stroke-width="2"/><path fill="none" stroke="#3a3a3a" stroke-width="2" d="M3 12h18M12 3c3 3 3 15 0 18M12 3c-3 3-3 15 0 18"/></svg>
          </span>www.ridgelinebuild.com
        </li>
      </ul>
      <p class="registrations">Lic. No. 4412 908 135<br>ABN 5820 331 476</p>
    </div>
  </section>
</main>
</body>
</html>
```